Start up business website

IT Support provider that caters towards law enforcement / police departments. We'll offer remote IT support, backup / recovery services and cyber security. Will add updates soon.

Target Market(s)

Police departments / Law Enforcement

Coding

Coded - Design and coding required

Number of Pages Required

5+ page

Other font styles liked:
• Use font style in uploaded logo

Colors
0054AA
0677BA
7BADD7
CADEEF
E8F1F8

```html
<!DOCTYPE html>
<html lang="en">
<head>
<meta charset="utf-8">
<title>Bastion Tech Services</title>
<link href="https://fonts.googleapis.com/css2?family=Michroma&family=Roboto:ital,wght@0,400;0,500;1,400&display=swap" rel="stylesheet">
<style>
:root{
  --navy:#0b2699;
  --navy-deep:#081c86;
  --blue:#0054AA;
  --blue-mid:#0677BA;
  --blue-soft:#7BADD7;
  --blue-pale:#CADEEF;
  --blue-mist:#E8F1F8;
  --bg-light:#eef3fa;
  --ink:#333a44;
  --grey:#555c66;
  --grey-light:#b5b9c0;
  --white:#ffffff;
  --display:"Michroma",sans-serif;
  --body:"Roboto",sans-serif;
}
*{box-sizing:border-box;margin:0;padding:0}
html,body{width:1200px;height:4252px;overflow:hidden;background:var(--white)}
body{font-family:var(--body);color:var(--ink)}
.canvas{position:relative;width:1200px;height:4252px;overflow:hidden}
.abs{position:absolute}
.display{font-family:var(--display);text-transform:uppercase;letter-spacing:1px}

/* header */
.brand{left:150px;top:26px;display:flex;align-items:center;gap:12px}
.brand-dot{width:38px;height:38px;border-radius:50%;background:var(--blue)}
.brand-name{font-family:var(--display);font-size:30px;color:var(--blue);letter-spacing:1px}
.contact-item{display:flex;align-items:center;gap:12px;white-space:nowrap}
.contact-icon{flex:0 0 44px;width:44px;height:44px;border-radius:50%;border:3px solid var(--blue);display:flex;align-items:center;justify-content:center}
.contact-label{font-family:var(--display);font-size:12px;color:var(--grey);line-height:17px}
.contact-value{font-family:var(--display);font-size:12px;color:var(--blue);line-height:17px}
.nav{left:0;top:91px;width:1200px;height:69px;background:var(--navy)}
.nav a{position:absolute;top:25px;font-family:var(--display);font-size:15px;color:var(--white);text-decoration:none;letter-spacing:1px;white-space:nowrap}
.nav a.active::after{content:"";position:absolute;left:0;right:0;top:34px;height:3px;background:var(--white)}

/* hero */
.hero{left:0;top:160px}
.hero-title{left:150px;top:345px;color:var(--white);font-family:var(--display)}
.hero-title .big{font-size:78px;line-height:100px;letter-spacing:2px}
.hero-title .small{font-size:30px;line-height:40px;letter-spacing:3px}

/* about */
.about-art{left:150px;top:900px;width:355px;height:430px;border-radius:40px;border:8px solid #a4a9b2;background:radial-gradient(circle at 60% 45%,#35b8f5,#0b5fc4 55%,#07307f)}
.eyebrow{font-family:var(--display);font-size:34px;color:#8a8f97}
.heading{font-family:var(--display);color:var(--blue);font-size:34px;line-height:44px;text-transform:uppercase;font-weight:400}
.copy{font-size:16px;line-height:22.5px;color:var(--ink)}
.btn{display:inline-block;font-family:var(--display);font-size:15px;color:var(--white);background:var(--blue);padding:16px 18px;letter-spacing:1px;text-transform:uppercase}

/* offer */
.offer{left:0;top:1410px;width:1200px;height:722px;background:linear-gradient(180deg,var(--blue-mist),#f4f7fb 60%,#e6ecf4)}
.section-title{width:1200px;text-align:center;font-family:var(--display);font-size:36px;color:var(--blue);text-transform:uppercase}
.card{background:var(--white);box-shadow:0 4px 16px rgba(40,70,130,.08);text-align:center}
.card-img{margin:24px auto 0;width:234px;height:215px}
.card h3{font-family:var(--display);font-weight:400;font-size:19px;line-height:22px;color:var(--blue);margin-top:20px;text-transform:uppercase}
.card p{font-size:14px;line-height:18px;color:var(--grey);margin:12px 22px 0}
.card .more{font-family:var(--display);font-size:12px;color:var(--grey-light);margin-top:18px;display:block}

/* why */
.why-text{left:718px;top:2235px;width:330px;color:var(--white)}
.why-text h2{font-family:var(--display);font-weight:400;font-size:34px;line-height:46px}
.why-text p{font-size:16px;line-height:22.5px;margin-top:14px}
.why-text .btn{background:#1148c4;margin-top:28px;padding:16px 20px}

/* reviews */
.quote-mark{font-family:Georgia,serif;font-size:210px;color:#e4e6ea;line-height:1}
.review-text{left:220px;top:2826px;width:520px;font-style:italic;font-size:16px;line-height:22.5px;color:#8a8f97}
.reviewer{left:220px;top:2935px;font-family:var(--display);font-size:20px;color:var(--blue)}
.dots{left:231px;top:3009px;display:flex;gap:12px}
.dots span{width:33px;height:4px;background:#c8cbd1}
.dots span.on{background:var(--blue)}
.portrait{left:767px;top:2648px;width:284px;height:396px;border-radius:60px 60px 140px 140px;border:10px solid #9da2ab;background:linear-gradient(160deg,#1b3fc0,#0a2488)}

/* news */
.news{left:0;top:3100px;width:1200px;height:800px;background:linear-gradient(180deg,var(--blue-mist),#f2f5fa)}
.news-card{background:var(--white);box-shadow:0 4px 16px rgba(40,70,130,.08)}
.news-title{font-family:var(--display);color:#3d4148;text-transform:uppercase}
.news-date{font-family:var(--display);color:var(--blue);text-transform:uppercase}

/* footer */
.footer-col h4{font-family:var(--display);font-weight:400;font-size:20px;color:var(--white);letter-spacing:1px}
.footer-col li{list-style:none;font-size:14px;line-height:22.5px;color:var(--white);white-space:nowrap}
.divider{width:1px;background:rgba(255,255,255,.25)}
.social{display:flex;align-items:center;gap:12px;margin-top:16px;font-size:14px;color:var(--white)}
.social span{width:30px;height:30px;border-radius:50%;background:var(--blue-mid)}
</style>
</head>
<body>
<div class="canvas">

  <!-- header -->
  <div class="abs brand"><div class="brand-dot"></div><div class="brand-name">BASTION</div></div>
  <div class="abs contact-item" style="left:558px;top:22px">
    <div class="contact-icon"><svg width="22" height="16" viewBox="0 0 22 16"><rect x="1" y="1" width="20" height="14" rx="2" fill="none" stroke="#0054AA" stroke-width="2"/><path d="M1 2 L11 9 L21 2" fill="none" stroke="#0054AA" stroke-width="2"/></svg></div>
    <div><div class="contact-label">EMAIL:</div><div class="contact-value">INFO@BASTION.COM</div></div>
  </div>
  <div class="abs contact-item" style="left:833px;top:22px">
    <div class="contact-icon"><svg width="20" height="20" viewBox="0 0 24 24"><path d="M6.6 10.8a15 15 0 0 0 6.6 6.6l2.2-2.2a1 1 0 0 1 1-.25 11.4 11.4 0 0 0 3.6.57 1 1 0 0 1 1 1V20a1 1 0 0 1-1 1A17 17 0 0 1 3 4a1 1 0 0 1 1-1h3.5a1 1 0 0 1 1 1c0 1.25.2 2.45.57 3.57a1 1 0 0 1-.25 1z" fill="#0054AA"/></svg></div>
    <div><div class="contact-label">CALL US:</div><div class="contact-value">555 -010 4477</div></div>
  </div>
  <nav class="abs nav">
    <a class="active" style="left:267px">HOME</a>
    <a style="left:376px">ABOUT</a>
    <a style="left:497px">SERVICES</a>
    <a style="left:647px">NEWS</a>
    <a style="left:752px">TESTIMONIALS</a>
    <a style="left:952px">CONTACT</a>
  </nav>

  <!-- hero -->
  <svg class="abs hero" width="1200" height="690" viewBox="0 0 1200 690" role="img" aria-label="Photo of operators at computer workstations in a security operations centre">
    <defs>
      <linearGradient id="heroFill" x1="0" y1="0" x2="1" y2="1">
        <stop offset="0" stop-color="#2d4b66"/><stop offset=".5" stop-color="#1b3146"/><stop offset="1" stop-color="#0f1c2a"/>
      </linearGradient>
    </defs>
    <path d="M0 0 H1200 V516 H940 C860 540 760 660 600 665 C440 660 340 540 260 516 H0 Z" fill="url(#heroFill)"/>
    <path d="M240 520 C340 548 440 680 600 682 C760 680 860 548 960 520" fill="none" stroke="#1c4fc0" stroke-width="9"/>
    <path d="M960 520 C1040 505 1120 505 1200 510" fill="none" stroke="#c9d6ec" stroke-width="4"/>
  </svg>
  <div class="abs hero-title"><div class="big">BASTION</div><div class="small">TECH SERVICES</div></div>

  <!-- about -->
  <div class="abs about-art" role="img" aria-label="Shield emblem filled with a glowing blue digital fingerprint"></div>
  <div class="abs" style="left:574px;top:888px;width:470px">
    <div class="eyebrow">ABOUT</div>
    <h1 class="heading" style="margin-top:16px">Bastion Tech<br>Services</h1>
    <p class="copy" style="margin-top:22px">Lorem ipsum dolor sit amet, consectetur adipiscing elit, sed do eiusmod tempor incididunt ut labore et dolore magna aliqua. Ut enim ad minim veniam, quis nostrud exercitation ullamco labb vris nisi ut aliquip ex ea commodo consequat. Duis aute irure dolor in reprehenderit in voluptLorem ipsum dolor sit amet, consectetur adipiscing elit, sed do eiusmod tempor incididunt ut labore et dolore magna aliqua. Ut enim ad minim veniam, q uis nostrud exercitation ullamco laboris nis.</p>
    <a class="btn" style="margin-top:26px">Read &nbsp;More</a>
  </div>

  <!-- offer -->
  <section class="abs offer">
    <h2 class="abs section-title" style="top:80px;font-weight:400">What We Offer</h2>
    <div class="abs card" style="left:150px;top:170px;width:280px;height:447px">
      <div class="card-img" role="img" aria-label="Photo of a support agent wearing a headset at a computer" style="background:linear-gradient(160deg,#b9c9dc,#4a5e78)"></div>
      <h3>Remote IT<br>Support</h3>
      <p>Lorem ipsum dolor sit amet, consectetur adipiscing elsed do eiusmod tempor incidt ut labore et dolore magna</p>
      <span class="more">READ MORE</span>
    </div>
    <div class="abs card" style="left:459px;top:170px;width:280px;height:447px">
      <div class="card-img" role="img" aria-label="Photo of a hand touching a digital backup interface" style="background:linear-gradient(160deg,#1d3a66,#0a1830)"></div>
      <h3>Backup /<br>Recovery<br>Services</h3>
      <p>Lorem ipsum dolor sit amet, consectetur adipiscing elsed do eiusmod tempor inci.</p>
      <span class="more">READ MORE</span>
    </div>
    <div class="abs card" style="left:766px;top:170px;width:280px;height:447px">
      <div class="card-img" role="img" aria-label="Glowing blue digital fingerprint" style="background:radial-gradient(circle,#3bc4f7,#0a59b8 60%,#062a70)"></div>
      <h3>Cyber<br>Security</h3>
      <p>Lorem ipsum dolor sit amet, consectetur adipiscing elsed do eiusmod tempor incidt ut labore et dolore magna</p>
      <span class="more">READ MORE</span>
    </div>
  </section>

  <!-- why choose us -->
  <svg class="abs" style="left:0;top:2132px" width="1200" height="545" viewBox="0 0 1200 545">
    <defs>
      <radialGradient id="circuit" cx="0.3" cy="0.42" r="0.6">
        <stop offset="0" stop-color="#2a7fe8"/><stop offset=".45" stop-color="#1140b8"/><stop offset="1" stop-color="#0a2496"/>
      </radialGradient>
    </defs>
    <path d="M0 0 H1200 V483 L0 543 Z" fill="#0b2699"/>
    <path d="M0 0 H693 V508 L0 543 Z" fill="url(#circuit)" role="img" aria-label="Blue circuit board pattern around a glowing emblem"/>
  </svg>
  <div class="abs why-text">
    <h2>WHY<br>CHOOSE US?</h2>
    <p>Lorem ipsum dolor sit amet, consectetur adi piscing elit, sed do eiusmod tempor incidid unt ut labore et dolore magna aliqua. Ut enim ad minim veniam, quis nostrud exercitation ullamco labb vris nisi ut aliquip ex ea com modo consequatuis aute irure .</p>
    <a class="btn">Read &nbsp;More</a>
  </div>

  <!-- reviews -->
  <h2 class="abs display" style="left:478px;top:2722px;font-size:36px;color:var(--blue);font-weight:400">Reviews</h2>
  <div class="abs quote-mark" style="left:96px;top:2760px">&ldquo;</div>
  <p class="abs review-text">Lorem ipsum dolor sit amet, consectetur adi piscing elit, sed do eiusmod tempor incidid unt ut labore et dolore magna aliqua. Ut enim ad minim veniam, quis nostrud exercitation ullamco labb vris nisi ut aliquip ex ea com modo consequatuis aute irure .</p>
  <div class="abs reviewer">DANA WHITFIELD</div>
  <div class="abs quote-mark" style="left:652px;top:2900px">&rdquo;</div>
  <div class="abs dots"><span class="on"></span><span></span><span></span><span></span></div>
  <div class="abs portrait" role="img" aria-label="Portrait of a smiling client in a grey suit inside a shield frame"></div>

  <!-- news -->
  <section class="abs news">
    <h2 class="abs section-title" style="top:82px;font-weight:400">Latest News</h2>
    <div class="abs news-card" style="left:150px;top:172px;width:490px;height:449px">
      <div role="img" aria-label="Photo of operators at a security operations centre" style="margin:25px 0 0 23px;width:446px;height:214px;background:linear-gradient(160deg,#3a5670,#142636)"></div>
      <div class="news-title" style="margin:36px 0 0 23px;font-size:20px;line-height:24px">Finibus Bonorum et<br>Malorum</div>
      <p style="margin:20px 23px 0;font-size:14px;line-height:18px;color:var(--grey)">Lorem ipsum dolor sit amet, consectetur adipiscing elit, sed do eiusmod tempor incididunt ut labore et dolore magna aliqua. Ut enim ad minim veniam, quis nostrud exercitatio.</p>
      <div class="news-date" style="margin:20px 0 0 23px;font-size:15px">Nov 10 2021</div>
    </div>
    <div class="abs news-card" style="left:660px;top:172px;width:386px;height:218px">
      <div class="abs" role="img" aria-label="Photo of a police officer at night with blue lights" style="left:20px;top:25px;width:170px;height:165px;background:linear-gradient(160deg,#1a3a8a,#0a1530)"></div>
      <div class="abs news-title" style="left:216px;top:34px;font-size:16px;line-height:21px">Finibus Bo<br>Malorum</div>
      <p class="abs" style="left:216px;top:92px;width:150px;font-size:13px;line-height:17px;color:var(--grey)">Lorem ipsum dolor sit amet, consectetur ad ipiscing elit, sed.</p>
      <div class="abs news-date" style="left:216px;top:164px;font-size:13px">Nov 10 2021</div>
    </div>
    <div class="abs news-card" style="left:660px;top:405px;width:386px;height:216px">
      <div class="abs" role="img" aria-label="Photo of golden scales of justice and a gavel" style="left:20px;top:22px;width:170px;height:165px;background:linear-gradient(160deg,#e8d9c4,#8a6a3a)"></div>
      <div class="abs news-title" style="left:216px;top:34px;font-size:16px;line-height:21px">Finibus Bo<br>Malorum</div>
      <p class="abs" style="left:216px;top:92px;width:150px;font-size:13px;line-height:17px;color:var(--grey)">Lorem ipsum dolor sit amet, consectetur ad ipiscing elit, sed.</p>
      <div class="abs news-date" style="left:216px;top:164px;font-size:13px">Nov 10 2021</div>
    </div>
  </section>

  <!-- footer -->
  <svg class="abs" style="left:0;top:3808px" width="1200" height="444" viewBox="0 0 1200 444"><path d="M0 55 L1200 0 V444 H0 Z" fill="#0b2699"/></svg>
  <div class="abs" style="left:150px;top:3990px;display:flex;align-items:center;gap:10px">
    <div style="width:30px;height:30px;border-radius:50%;background:var(--white)"></div>
    <div style="font-family:var(--display);font-size:24px;color:var(--white)">BASTION</div>
  </div>
  <div class="abs divider" style="left:353px;top:3855px;height:302px"></div>
  <div class="abs divider" style="left:630px;top:3845px;height:312px"></div>
  <div class="abs divider" style="left:853px;top:3840px;height:317px"></div>
  <div class="abs footer-col" style="left:393px;top:3912px">
    <h4>CONTACT</h4>
    <ul style="margin-top:14px">
      <li>&#9679;&nbsp; Bastion Tech Services</li>
      <li style="padding-left:21px">42 Harbor Lane</li>
      <li style="padding-left:21px">Northvale 10421</li>
      <li style="margin-top:22px">&#9742; Phone:555 010 2233</li>
      <li style="margin-top:22px">&#9993; Email:hello@bastiontech.com</li>
    </ul>
  </div>
  <div class="abs footer-col" style="left:678px;top:3912px">
    <h4>LINKS</h4>
    <ul style="margin-top:14px">
      <li>Contact Us</li><li>About us</li><li>Sevices</li><li>Terms &amp; Conditions</li><li>Privacy Policy</li><li>Blog</li><li>Sitemap</li>
    </ul>
  </div>
  <div class="abs footer-col" style="left:886px;top:3912px">
    <h4>FOLLOW US</h4>
    <div class="social" style="margin-top:16px"><span></span>Newsfeed</div>
    <div class="social"><span></span>Updates</div>
    <div class="social"><span></span>Network</div>
  </div>
  <div class="abs" style="left:150px;top:4158px;width:898px;height:1px;background:rgba(255,255,255,.25)"></div>
  <div class="abs" style="left:0;top:4196px;width:1200px;text-align:center;font-size:15px;color:var(--white)">Copyright &copy; 2021 All Right Reserved</div>

</div>
</body>
</html>
```